Annual review for The Birchmoor Collective

The Birchmoor Collective is a small public relations agency in London specialising in corporate and public affairs. Most of our work is international and we have a strong connection to South Africa. We would like to prepare a short annual review for 2016. The review will serve as both a review of our activities in 2016, and as a credentials document. Content then will include:
1. An introduction to the business
2. Who we are
3. Projects and clients undertaken in 2016
4. News and views
We imagine it will be used mostly as a pdf but would like it to be suitable for print. We envisage it to be about 8 pages long. The design look and feel should convey a business, while small, of stature. We shall include some of our client logos but we would welcome the use of some photography / imagery to have visual impact (although we don't have very much of our own!). The corporate look and feel is white, grey and black.

Industry/Entity Type

Public Relation

Font styles to use
Sans Serif

Requirements
Must have
• My project must convey a business with flair and gravitas, that punches above its weight.
Nice to have
• Thoughtful use of imagery.

```html
<!DOCTYPE html>
<html lang="en">
<head>
<meta charset="utf-8">
<title>The Birchmoor Collective – Annual Review 2016</title>
<link href="https://fonts.googleapis.com/css2?family=Open+Sans:ital,wght@0,300;0,400;0,700;1,400&display=swap" rel="stylesheet">
<style>
:root{
  --ink:#3a3a3a;
  --title:#4a4a4a;
  --brand:#6b6b6b;
  --accent:#1f9bd1;
  --paper:#ffffff;
  --mid:#9a9a9a;
  --light:#d9d9d9;
}
*{margin:0;padding:0;box-sizing:border-box}
html,body{width:1200px;height:849px;overflow:hidden;background:var(--paper)}
body{font-family:"Open Sans",Arial,sans-serif;color:var(--ink);position:relative}
.spread{position:relative;width:1200px;height:849px}
.brand{position:absolute;top:46px;display:flex;align-items:center;gap:7px;font-weight:700;font-size:16px;color:var(--brand);letter-spacing:-.2px}
.brand-dot{width:20px;height:20px;border:2px solid var(--brand);border-radius:50%}
.page-title{position:absolute;top:110px;font-weight:300;font-size:40px;color:var(--title);letter-spacing:-.3px}
.block{position:absolute}
.block h2{font-weight:400;font-size:12.6px;line-height:14.6px;color:var(--accent);margin-bottom:11px}
.block p{font-size:9.1px;line-height:10.9px;color:var(--ink)}
.block p.caption{font-style:italic;margin-bottom:10px}
.media{display:block;margin-bottom:12px}
.clip{background:linear-gradient(160deg,#e6e6e6,#b9b9b9 55%,#d2d2d2)}
.photo{background:linear-gradient(150deg,#8a8a8a,#3c3c3c 60%,#6f6f6f)}
.mark{display:block;margin-bottom:12px}
.news-photo{position:absolute;left:600px;top:543px;width:600px;height:306px;background:linear-gradient(155deg,#f2f2f2 0%,#cfcfcf 35%,#eeeeee 55%,#a9a9a9 80%,#dcdcdc 100%)}
.folio{position:absolute;top:805px;font-size:7.4px;letter-spacing:2px;color:var(--mid)}
.folio .num{color:var(--accent)}
</style>
</head>
<body>
<main class="spread">

  <!-- left page -->
  <div class="brand" style="left:58px"><span class="brand-dot"></span>The Birchmoor Collective</div>
  <h1 class="page-title" style="left:58px">2016 highlights</h1>

  <section class="block" style="left:58px;top:187px;width:155px">
    <h2>Highlighting illicit financial flows in Africa</h2>
    <div class="media clip" style="width:99px;height:73px" role="img" aria-label="Newspaper clipping about a disputed debt"></div>
    <p>We were retained to provide public relations and public affairs advice to a Tanzanian investment firm in a major legal dispute with a leading international bank. The dispute related to an investment in ‘distressed debt’ and led to dual legal proceedings in Tanzania and the UK. As part of the assignment the Birchmoor Collective was asked to highlight the impact of illicit financial flows out of Tanzania, and Africa.</p>
  </section>

  <section class="block" style="left:58px;top:466px;width:155px">
    <h2>Challenging ELA’s<br>Club Finance Rules</h2>
    <div class="media clip" style="width:98px;height:106px" role="img" aria-label="Newspaper clipping showing a sports lawyer"></div>
    <p>The Birchmoor Collective continued to provide public relations support to sports competition lawyer Laurent Deville in his work on a legal challenge against the European football regulator ELA and its Club Finance Rules (CFR). At a hearing in 2015 the Belgian court upheld the complaint, referring the case to the European Court of Justice (ECJ) for a final ruling. Separate cases have now been brought in France and Switzerland.</p>
  </section>

  <section class="block" style="left:224px;top:187px;width:155px">
    <h2>Promoting the Halabi<br>Foundation</h2>
    <div class="media photo" style="width:105px;height:73px" role="img" aria-label="Photograph of a journalist and his lawyer speaking at an event"></div>
    <p class="caption">Tarek Halabi and his lawyer Nadia Farrow speaking at an event at the Meridian Press Club, London organised by The Birchmoor Collective. (Photograph courtesy of The Meridian Press Club)</p>
    <p>The Birchmoor Collective undertook the assignment of campaigning for the release of Gulfwave News bureau chief Canadian Tarek Halabi imprisoned in Egypt. We worked with Halabi’s legal team led by Nadia Farrow in lobbying organizations such as the UN, EU, and others while maintaining media profile of the story. Halabi was granted a presidential pardon in September 2015. Through 2016, we continued to support Halabi in raising awareness of his experience in Cairo.</p>
  </section>

  <section class="block" style="left:224px;top:552px;width:155px">
    <h2>Reviewing the NSAW’s<br>governance</h2>
    <svg class="mark" width="62" height="33" viewBox="0 0 62 33" role="img" aria-label="Client badge"><rect x="1" y="1" width="60" height="31" rx="9" fill="#2b2b2b"/></svg>
    <p>The Birchmoor Collective was approached by the National Society for Animal Welfare (NSAW) to assist it in a review of its governance. Established in 1824, the NSAW is one of the largest and best known charities in the UK. We were asked to look at existing governance structures in a number of organisations across the charitable sector as part of best practice research. The work is expected to continue into 2017.</p>
  </section>

  <section class="block" style="left:390px;top:187px;width:155px">
    <h2>Supporting Kloofvale’s<br>stakeholder outreach</h2>
    <svg class="mark" width="60" height="68" viewBox="0 0 60 68" role="img" aria-label="Client badge"><rect x="24" y="2" width="34" height="40" fill="#8f8f8f"/></svg>
    <p>Kloofvale University is one of South Africa’s top universities. In 2016 it appointed The Birchmoor Collective to assist it in mapping the funding landscape in the UK. We undertook extensive desk research into UK-based foundations and trusts that disburse major grants and awards for educational purposes. We advised the Vice-Chancellor and Corporate Development team on elements of his UK visit to meet funding institutions, and other influencers.</p>
  </section>

  <section class="block" style="left:390px;top:488px;width:155px">
    <h2>Leading in water</h2>
    <svg class="mark" width="50" height="80" viewBox="0 0 50 80" role="img" aria-label="Partner badge"><circle cx="25" cy="46" r="22" fill="#8f8f8f"/></svg>
    <p>In 2016 The Birchmoor Collective’s Adrian Mercer was seconded into the Global Water Resources Forum (GWRF) as its Executive Director. Established in 1971, the GWRF is a membership organisation that represents the interests of the water science and policy community. Adrian was charged with managing the organisation’s relocation to Paris and overseeing the preparations for its triennial Global Water Summit which will be held in May 2017 in Cancun, Mexico.</p>
  </section>

  <div class="folio" style="left:58px"><span class="num">05</span> &nbsp;|&nbsp; ANNUAL REVIEW 2016</div>
  <div class="folio" style="left:423px">www.birchmoorcollective.com</div>

  <!-- right page -->
  <div class="brand" style="left:657px"><span class="brand-dot"></span>The Birchmoor Collective</div>
  <h1 class="page-title" style="left:657px">In the News</h1>

  <section class="block" style="left:657px;top:187px;width:236px">
    <h2>Farming in Africa</h2>
    <p>In March, a letter on the topic of agriculture in Africa written by Adrian Mercer was published in The Global Ledger. Highlighting how water resilience and water security is key to Africa’s booming agricultural sector, Adrian explained that Africa’s water is shared across 13 river basins that are mostly accessed by five or more countries, prompting the need for greater cooperation as water scarcity increases.</p>
  </section>

  <section class="block" style="left:657px;top:310px;width:236px">
    <h2>Water corruption</h2>
    <p>Water corruption leaves millions mired in misery – that was the message from Adrian Mercer in an article published in The Daily Current. Adrian used an anti-corruption summit hosted by the then Prime Minister to draw attention to the water sector’s susceptibility to graft. Explaining how water cuts across a range of portfolios and disciplines, he writes that this leads to different political and governmental agencies having often overlapping and, at times, conflicting responsibilities.</p>
  </section>

  <section class="block" style="left:906px;top:187px;width:240px">
    <h2>Owen Harcourt joins the team</h2>
    <p>In September The Birchmoor Collective welcomed Owen Harcourt as a new member of the team. Owen joined from UK-wide law firm Lyle Ashby. Owen studied journalism and is a graduate of both Eastvale University and the Coastlands University in South Africa. He has also worked for Motorshow Live in South Africa, and interned at The Evening Courier newspaper.</p>
  </section>

  <section class="block" style="left:906px;top:299px;width:240px">
    <h2>Focus on Fukushima</h2>
    <p>Writing in the Pacific Herald, Adrian Mercer marked the fifth anniversary of the pacific earthquake and tsunami to highlight the dilemma of water in Fukushima, a highly complex post-disaster situation. He set out the challenges confronting policymakers as they consider the options for the long-term management of nearly a million tons of contaminated water.</p>
  </section>

  <section class="block" style="left:906px;top:412px;width:240px">
    <h2>Forging a Canadian partnership</h2>
    <p>In 2016 we established a partnership with Vancouver-based law firm Harrow &amp; Lindqvist and its consulting division, Northline Advisory Inc. We believe our collective international experience harnessing legal and strategic expertise across a range of sectors will be of value to clients both sides of the Atlantic.</p>
  </section>

  <div class="news-photo" role="img" aria-label="Black and white photograph of a stack of folded newspapers"></div>

</main>
</body>
</html>
```